Postcard for commercial concrete cleaning company that will be mailed to business customers

A 6x9 postcard that will be mailed out to businesses who have concrete (sidewalks, drive thrus, dumpster pads, etc) that need periodic pressure washing to keep clean. Our current customers are majority restaurants. We are able to remove gum and grease from concrete which is difficult for much of our competitors. We work at night when the businesses are closed or slow if 24hr.

Target Market(s)

This will go to restaurants, banks, gas stations and other retail locations.

Colors

Designer to choose colors to be used in the design.

Requirements
Must have
• Logo. A headline that mentions commercial concrete cleaning so recipients will know at a glance what we do
Nice to have
• The image included is of a fast food doorway that is half cleaned, the right side. Something like "Dirty Doorway?" may make sense.
• We specialize is maintenance concrete cleaning where we come on a regular basis so I like phrase keep your concrete clean, or keep your business clean. something like that.

```html
<!DOCTYPE html>
<html lang="en">
<head>
<meta charset="utf-8">
<title>Brightline Concrete Care – Postcard</title>
<link href="https://fonts.googleapis.com/css2?family=Anton&family=Montserrat:wght@500;600;700;800&family=Roboto+Condensed:wght@700&display=swap" rel="stylesheet">
<style>
  :root{
    --page-bg:#d6d7da;
    --blue-deep:#1f2d6e;
    --blue-mid:#2a55a6;
    --blue-light:#3b86cc;
    --headline-blue:#1d4fb8;
    --ink:#1b1b1b;
    --navy-text:#1e3f8a;
    --silver-light:#f2f2f2;
    --silver-mid:#c9c9c9;
    --charcoal:#2b2b2b;
    --white:#ffffff;
  }
  html,body{margin:0;padding:0;width:1200px;height:1200px;overflow:hidden;background:var(--page-bg);}
  .canvas{position:relative;width:1200px;height:1200px;}
  .postcard{position:absolute;box-shadow:0 8px 22px rgba(0,0,0,.28);display:block;}
  .postcard--front{left:230px;top:82px;width:742px;height:500px;}
  .postcard--back{left:230px;top:643px;width:751px;height:506px;}
  .headline{font-family:'Anton',sans-serif;fill:var(--headline-blue);stroke:var(--white);stroke-width:3;paint-order:stroke;}
  .tagline{font-family:'Montserrat',sans-serif;font-weight:800;fill:var(--white);}
  .badge-small{font-family:'Montserrat',sans-serif;font-weight:600;fill:var(--white);}
  .badge-big{font-family:'Montserrat',sans-serif;font-weight:800;fill:var(--white);}
  .brand{font-family:'Montserrat',sans-serif;font-weight:700;fill:var(--navy-text);}
  .phone{font-family:'Roboto Condensed',sans-serif;font-weight:700;fill:var(--ink);}
  .intro{font-family:'Montserrat',sans-serif;font-weight:700;fill:var(--white);}
  .photo-label{font-family:'Montserrat',sans-serif;font-weight:700;fill:var(--charcoal);}
  .services-title{font-family:'Montserrat',sans-serif;font-weight:600;fill:var(--white);letter-spacing:.5px;}
  .services-list{font-family:'Montserrat',sans-serif;font-weight:600;fill:var(--white);}
  .contact-cta{font-family:'Montserrat',sans-serif;font-weight:700;fill:var(--navy-text);}
  .phone-back{font-family:'Montserrat',sans-serif;font-weight:700;fill:var(--ink);}
</style>
</head>
<body>
<div class="canvas">

  <!-- Front of postcard -->
  <svg class="postcard postcard--front" viewBox="0 0 927 625" xmlns="http://www.w3.org/2000/svg">
    <defs>
      <linearGradient id="doorwayPhoto" x1="0" y1="0" x2="1" y2="0">
        <stop offset="0" stop-color="#9c8a6a"/>
        <stop offset=".45" stop-color="#b5a58a"/>
        <stop offset=".55" stop-color="#d3cdbf"/>
        <stop offset="1" stop-color="#ddd8cc"/>
      </linearGradient>
      <linearGradient id="blueBand" x1="0" y1="0" x2="1" y2="0">
        <stop offset="0" stop-color="var(--blue-light)"/>
        <stop offset=".55" stop-color="var(--blue-mid)"/>
        <stop offset="1" stop-color="var(--blue-deep)"/>
      </linearGradient>
      <linearGradient id="silverBand" x1="0" y1="0" x2="0" y2="1">
        <stop offset="0" stop-color="var(--silver-light)"/>
        <stop offset="1" stop-color="var(--silver-mid)"/>
      </linearGradient>
      <linearGradient id="badgeRing" x1="0" y1="0" x2="0" y2="1">
        <stop offset="0" stop-color="#ffffff"/>
        <stop offset="1" stop-color="#8a8a8a"/>
      </linearGradient>
      <radialGradient id="badgeFace" cx=".5" cy=".35" r=".7">
        <stop offset="0" stop-color="#5a5a5a"/>
        <stop offset="1" stop-color="#1e1e1e"/>
      </radialGradient>
    </defs>

    <rect class="photo-area" role="img" aria-label="Photo of a restaurant doorway with concrete half pressure washed, right side clean" x="0" y="0" width="927" height="360" fill="url(#doorwayPhoto)"/>

    <path d="M0 305 C 250 345 520 260 927 230 L927 625 L0 625 Z" fill="#8e8e8e"/>
    <path d="M0 318 C 250 360 520 275 927 250 L927 625 L0 625 Z" fill="#1c1c1c"/>
    <path d="M0 335 C 260 370 540 290 927 270 L927 625 L0 625 Z" fill="url(#blueBand)"/>
    <path d="M0 503 C 120 485 200 470 300 478 C 520 495 700 520 927 505 L927 625 L0 625 Z" fill="url(#silverBand)"/>

    <text class="headline" x="62" y="140" font-size="78">DIRTY</text>
    <text class="headline" x="62" y="235" font-size="78">DOORWAY?</text>

    <g class="availability-badge">
      <circle cx="766" cy="273" r="88" fill="url(#badgeRing)"/>
      <circle cx="766" cy="273" r="79" fill="url(#badgeFace)"/>
      <text class="badge-small" x="766" y="252" font-size="20" text-anchor="middle">Available</text>
      <text class="badge-big" x="766" y="296" font-size="44" text-anchor="middle">24HR</text>
    </g>

    <text class="tagline" x="66" y="446" font-size="47">KEEP YOUR CONCRETE CLEAN</text>

    <text class="brand brand-name" x="57" y="580" font-size="30">Brightline Concrete Care</text>

    <text class="phone" x="860" y="585" font-size="34" text-anchor="end">(555) 014-2290</text>
  </svg>

  <!-- Back of postcard -->
  <svg class="postcard postcard--back" viewBox="0 0 939 633" xmlns="http://www.w3.org/2000/svg">
    <defs>
      <linearGradient id="blueBack" x1="0" y1="0" x2="1" y2="1">
        <stop offset="0" stop-color="var(--blue-light)"/>
        <stop offset=".6" stop-color="var(--blue-mid)"/>
        <stop offset="1" stop-color="var(--blue-deep)"/>
      </linearGradient>
      <linearGradient id="silverBack" x1="0" y1="0" x2="0" y2="1">
        <stop offset="0" stop-color="var(--silver-light)"/>
        <stop offset="1" stop-color="var(--silver-mid)"/>
      </linearGradient>
      <linearGradient id="beforePhoto" x1="0" y1="0" x2="1" y2="1">
        <stop offset="0" stop-color="#a08c6c"/>
        <stop offset="1" stop-color="#b9a98c"/>
      </linearGradient>
      <linearGradient id="afterPhoto" x1="0" y1="0" x2="1" y2="1">
        <stop offset="0" stop-color="#e8e6df"/>
        <stop offset="1" stop-color="#c7c2b6"/>
      </linearGradient>
      <clipPath id="leftPanel">
        <path d="M0 0 H648 C 500 90 430 230 450 380 C 465 490 510 570 565 633 H0 Z"/>
      </clipPath>
    </defs>

    <rect x="0" y="0" width="939" height="633" fill="var(--white)"/>

    <g clip-path="url(#leftPanel)">
      <rect x="0" y="0" width="700" height="633" fill="url(#blueBack)"/>
      <path d="M0 478 C 200 455 380 455 700 490 L700 633 L0 633 Z" fill="#1c1c1c"/>
      <path d="M0 505 C 200 480 380 480 700 515 L700 633 L0 633 Z" fill="url(#silverBack)"/>
    </g>

    <text class="intro" font-size="24">
      <tspan x="60" y="53">We specialize in maintenance</tspan>
      <tspan x="60" y="84">concrete cleaning where we</tspan>
      <tspan x="60" y="115">come on a regular basis</tspan>
    </text>

    <rect class="photo-before" role="img" aria-label="Before photo: stained concrete walkway" x="57" y="142" width="177" height="125" rx="22" fill="url(#beforePhoto)" stroke="#ffffff" stroke-width="2"/>
    <rect class="photo-after" role="img" aria-label="After photo: clean pressure washed concrete walkway" x="243" y="142" width="177" height="125" rx="22" fill="url(#afterPhoto)" stroke="#ffffff" stroke-width="2"/>
    <rect x="128" y="238" width="106" height="29" rx="14.5" fill="#ffffff"/>
    <text class="photo-label" x="176" y="260" font-size="19" text-anchor="middle">Before</text>
    <rect x="243" y="238" width="100" height="29" rx="14.5" fill="#ffffff"/>
    <text class="photo-label" x="303" y="260" font-size="19" text-anchor="middle">After</text>

    <g class="services-pill">
      <rect x="117" y="306" width="218" height="42" rx="21" fill="#ffffff"/>
      <rect x="121" y="310" width="210" height="34" rx="17" fill="#2c2c2c"/>
      <text class="services-title" x="226" y="335" font-size="20" text-anchor="middle">OUR SERVICES</text>
    </g>
    <text class="services-list" font-size="21" text-anchor="middle">
      <tspan x="226" y="389">sidewalks, drive thrus</tspan>
      <tspan x="226" y="417">dumpster pads, etc</tspan>
    </text>

    <text class="contact-cta" x="233" y="544" font-size="24" text-anchor="middle">Contact Us Now</text>
    <text class="phone-back" x="233" y="593" font-size="44" text-anchor="middle">(555) 014-2290</text>

    <text class="brand brand-name-small" x="600" y="98" font-size="14">Brightline Concrete Care</text>

    <rect class="stamp-box" x="796" y="38" width="96" height="90" fill="none" stroke="#9a9a9a" stroke-width="1.5" stroke-dasharray="4 3"/>

    <g class="address-lines" stroke="#9a9a9a" stroke-width="1.5">
      <line x1="566" y1="219" x2="890" y2="219"/>
      <line x1="566" y1="270" x2="890" y2="270"/>
      <line x1="566" y1="324" x2="890" y2="324"/>
      <line x1="566" y1="378" x2="890" y2="378"/>
    </g>
  </svg>

</div>
</body>
</html>
```